A website for a Maltese Law Firm

Our law firm needs a website to further its business. The site should have a simple yet effective design. We would need the following sections: About us, Practice Areas, About Malta, Contact. These should be further split as follows:

About us: Our firm, Our values, What others say, Offices

Practice Areas: Crimimal, Citizenship & Residence, Harbour Passage Scheme, Criminal Defence, Civil Litigation, Arbitration and ADR, Commercial and Corporate, Media Law.

About Malta: just one section.

Contact: Just one section

We would also need a news feed at the front of the site to include latest news regarding our cases.

At the bottom we need a section for our Terms and a Privacy Statement.

Our logo is being attached.

Target Market(s)

All clients looking for legal assistance in Malta

Industry/Entity Type

Legal

Coding

Coded - Design and coding required

Number of Pages Required

1 page

Requirements
Must have
• It must be simple yet striking.

```html
<!DOCTYPE html>
<html lang="en">
<head>
<meta charset="utf-8">
<title>Dalmer &amp; Vossen Advocates</title>
<link href="https://fonts.googleapis.com/css2?family=Cinzel:wght@400;700&family=Lato:wght@400;700&display=swap" rel="stylesheet">
<style>
:root{
  --orange:#f7941d;
  --black:#1a1a1a;
  --ink:#222;
  --muted:#666;
  --grey-band:#ebebeb;
  --grey-panel:#e2e2e2;
  --light:#f4f4f4;
  --white:#fff;
}
*{margin:0;padding:0;box-sizing:border-box}
html,body{width:1200px;height:3220px;overflow:hidden;background:var(--white)}
body{position:relative;font-family:'Lato',Arial,sans-serif;color:var(--ink)}
.abs{position:absolute}
.serif{font-family:'Cinzel',Georgia,serif}

/* header */
.site-header{left:0;top:0;width:1200px;height:70px;background:var(--white);z-index:3}
.brand{left:99px;top:0;width:275px;height:78px;background:var(--black);border-bottom:4px solid var(--orange);display:flex;align-items:center;justify-content:center;color:var(--white);font-family:'Cinzel',serif;font-size:22px;letter-spacing:1px;font-weight:700}
.nav a{position:absolute;top:26px;font-family:'Cinzel',serif;font-size:13px;color:var(--ink);text-decoration:none;letter-spacing:.5px}
.nav a.active{color:var(--orange)}
.nav a.active::after{content:"";position:absolute;left:-8px;right:-8px;top:40px;height:3px;background:var(--orange)}
.search-btn{left:1069px;top:18px;width:32px;height:32px;background:var(--orange);display:flex;align-items:center;justify-content:center}

/* hero */
.hero{left:0;top:70px;width:1200px;height:530px;background:linear-gradient(90deg,#1d140f 0%,#3a2a22 40%,#4a4f56 62%,#2e3238 100%)}
.hero-title{left:99px;top:250px;color:var(--white);font-family:'Cinzel',serif;font-size:52px;line-height:64px;letter-spacing:1px}
.scroll-hint{left:600px;top:500px;width:22px;height:36px;border:2px solid #ddd;border-radius:11px}

/* section titles */
.section-title{left:0;width:1200px;text-align:center;font-family:'Cinzel',serif;font-size:36px;color:var(--ink)}
.section-title span{position:relative;padding:0 18px}
.section-title span::before,.section-title span::after{content:"";position:absolute;top:50%;width:130px;height:2px;background:var(--ink)}
.section-title span::before{right:100%}
.section-title span::after{left:100%}

.about-text{left:110px;top:732px;width:980px;text-align:center;font-size:14.5px;line-height:22px;color:var(--muted)}
.about-item{width:200px;text-align:center}
.about-item .ring{width:136px;height:136px;margin:0 auto;border-radius:50%;border:2px solid #e4e4e4;display:flex;align-items:center;justify-content:center}
.about-item p{margin-top:20px;font-size:21px;color:var(--ink)}

/* practice */
.practice-band{left:0;top:1073px;width:1200px;height:823px;background:var(--grey-band)}
.tile{width:250px;height:212px}
.tile .photo{width:100%;height:168px}
.tile .label{height:44px;background:var(--white);display:flex;align-items:center;justify-content:center;font-size:16px;color:var(--ink)}
.btn{background:var(--orange);color:var(--white);font-family:'Cinzel',serif;display:flex;align-items:center;justify-content:center;letter-spacing:1px}

/* about malta */
.malta-photo{left:99px;top:1975px;width:358px;height:309px;background:linear-gradient(135deg,#d9cbb8 0%,#6b6f7a 45%,#2b2f3c 100%)}
.malta-title{left:505px;top:1966px;font-family:'Cinzel',serif;font-size:36px;color:var(--ink)}
.malta-text{left:505px;top:2018px;width:600px;font-size:15px;line-height:21.5px;color:var(--muted)}
.malta-text p+p{margin-top:21px}

/* testimonials & sign in */
.testi-band{left:0;top:2325px;width:734px;height:524px;background:var(--grey-band)}
.signin-band{left:734px;top:2325px;width:466px;height:524px;background:var(--grey-panel)}
.quote{left:130px;top:2505px;width:580px;font-size:14px;line-height:22px;font-style:italic;color:var(--muted)}
.qmark{font-family:Georgia,serif;font-size:40px;color:var(--ink)}
.avatar{left:363px;top:2616px;width:80px;height:80px;border-radius:50%;background:linear-gradient(#5a4538,#2d2420)}
.stars{left:0;width:806px;top:2704px;text-align:center;color:var(--orange);font-size:16px;letter-spacing:2px}
.person{left:0;width:806px;top:2728px;text-align:center;font-size:14px;letter-spacing:.5px}
.person small{display:block;font-size:13px;color:var(--muted);margin-top:2px}
.field-label{left:766px;font-size:10px;color:var(--muted);letter-spacing:.5px}
.field{left:766px;width:335px;height:37px;background:var(--light);border:1px solid #d9d9d9}
.forgot{left:1015px;top:2598px;font-size:10px;font-style:italic;color:var(--orange)}

/* footer */
.footer-dark{left:0;top:2849px;width:1200px;height:335px;background:var(--black)}
.footer-panel{left:498px;top:2849px;width:603px;height:335px;background:#e8e8e8}
.footer-title{left:99px;top:2922px;color:var(--white);font-family:'Cinzel',serif;font-size:18px;letter-spacing:1px}
.footer-links a{position:absolute;color:var(--white);font-family:'Cinzel',serif;font-size:12px;text-decoration:none}
.footer-brand{left:498px;top:2989px;width:253px;height:49px;background:var(--black);border-bottom:3px solid var(--orange);color:var(--white);font-family:'Cinzel',serif;font-size:17px;font-weight:700;display:flex;align-items:center;justify-content:center}
.address{left:498px;top:3068px;width:290px;text-align:center;font-family:'Cinzel',serif;font-size:15px;font-weight:700;line-height:26px;color:var(--ink)}
.mail-link{left:498px;width:290px;top:3128px;text-align:center;color:var(--orange);font-size:15px;font-weight:700}
.phone{left:777px;font-family:'Cinzel',serif;font-size:16px;color:var(--ink);display:flex;align-items:center;gap:12px}
.bottom-bar{left:0;top:3184px;width:1200px;height:36px;background:var(--white);font-size:11px;color:var(--ink)}
.bottom-bar a{color:var(--ink);text-decoration:none;margin-right:22px}
</style>
</head>
<body>

<header class="site-header abs">
  <div class="brand abs">Dalmer &amp; Vossen</div>
  <nav class="nav">
    <a class="active" style="left:468px">Home</a>
    <a style="left:554px">About Us</a>
    <a style="left:668px">Practice Areas</a>
    <a style="left:824px">About Malta</a>
    <a style="left:968px">Contact</a>
  </nav>
  <div class="search-btn abs">
    <svg width="14" height="14" viewBox="0 0 14 14"><circle cx="6" cy="6" r="4.5" fill="none" stroke="#fff" stroke-width="2"/><line x1="9.5" y1="9.5" x2="13" y2="13" stroke="#fff" stroke-width="2"/></svg>
  </div>
</header>

<section class="hero abs" role="img" aria-label="Lawyer in a dark suit standing before shelves of law books"></section>
<h1 class="hero-title abs">Dalmer &amp; Vossen<br>Advocates</h1>
<div class="scroll-hint abs"></div>

<h2 class="section-title abs" style="top:665px"><span>About Us</span></h2>
<p class="about-text abs">Lorem ipsum dolor sit amet, consectetur adipisicing elit, sed do eiusmod tempor incididunt ut labore et dolore magna aliqua. Ut enim ad minim veniam, quis nostrud exercitation ullamco laboris nisi ut aliquip ex ea commodo consequat. Duis aute irure dolor in reprehenderit in voluptate velit esse cillum dolore eu fugiat nulla pariatur.</p>

<div class="about-item abs" style="left:147px;top:823px">
  <div class="ring"><svg width="64" height="60" viewBox="0 0 64 60" fill="#f7941d"><rect x="30" y="6" width="4" height="46"/><rect x="8" y="10" width="48" height="3"/><rect x="18" y="52" width="28" height="5"/><path d="M2 34h20l-10-20z" fill="none" stroke="#f7941d" stroke-width="2"/><path d="M2 34a10 6 0 0 0 20 0z"/><path d="M42 34h20l-10-20z" fill="none" stroke="#f7941d" stroke-width="2"/><path d="M42 34a10 6 0 0 0 20 0z"/></svg></div>
  <p>Our Firm</p>
</div>
<div class="about-item abs" style="left:377px;top:823px">
  <div class="ring"><svg width="64" height="56" viewBox="0 0 64 56" fill="#f7941d"><rect x="6" y="38" width="9" height="16"/><rect x="20" y="30" width="9" height="24"/><rect x="34" y="22" width="9" height="32"/><rect x="48" y="12" width="9" height="42"/><path d="M4 30L26 14l10 8L56 4" fill="none" stroke="#f7941d" stroke-width="3"/><path d="M50 2h8v8z"/></svg></div>
  <p>Our Values</p>
</div>
<div class="about-item abs" style="left:624px;top:823px">
  <div class="ring"><svg width="60" height="60" viewBox="0 0 60 60"><path d="M30 4a24 24 0 1 1-14 43l-10 9 3-14A24 24 0 0 1 30 4z" fill="#f7941d"/><rect x="19" y="24" width="22" height="3" fill="#fff"/><rect x="19" y="32" width="16" height="3" fill="#fff"/></svg></div>
  <p>What Others Say</p>
</div>
<div class="about-item abs" style="left:853px;top:823px">
  <div class="ring"><svg width="64" height="60" viewBox="0 0 64 60" fill="#f7941d"><circle cx="32" cy="8" r="6"/><rect x="24" y="16" width="16" height="12"/><rect x="2" y="28" width="60" height="6"/><rect x="8" y="34" width="48" height="24"/><path d="M32 38l3 6h6l-5 4 2 6-6-4-6 4 2-6-5-4h6z" fill="#fff"/></svg></div>
  <p>Offices</p>
</div>

<div class="practice-band abs"></div>
<h2 class="section-title abs" style="top:1148px"><span>Practice Areas</span></h2>

<div class="tile abs" style="left:99px;top:1226px"><div class="photo" role="img" aria-label="Hands in handcuffs on a table" style="background:linear-gradient(135deg,#3a2820,#b98a6a)"></div><div class="label">Crimimal</div></div>
<div class="tile abs" style="left:350px;top:1226px"><div class="photo" role="img" aria-label="Smiling woman holding a national flag" style="background:linear-gradient(135deg,#2d4c8a,#d7c3b0 55%,#4a7a3a)"></div><div class="label">Citizenship &amp; Residence</div></div>
<div class="tile abs" style="left:601px;top:1226px"><div class="photo" role="img" aria-label="Stacks of gold coins" style="background:linear-gradient(135deg,#5a78b8,#d8a440 60%,#8a5a20)"></div><div class="label">Harbour Passage Scheme</div></div>
<div class="tile abs" style="left:852px;top:1226px"><div class="photo" role="img" aria-label="Gavel resting on law books" style="background:linear-gradient(135deg,#e8e2d8,#8a4a28 60%,#3a2418)"></div><div class="label">Criminal Defence</div></div>

<div class="tile abs" style="left:99px;top:1458px"><div class="photo" role="img" aria-label="Empty courtroom bench with a flag" style="background:linear-gradient(135deg,#c9a27a,#6a3a20 60%,#2a1a12)"></div><div class="label">Civil Litigation</div></div>
<div class="tile abs" style="left:350px;top:1458px"><div class="photo" role="img" aria-label="Gavel in front of a striped flag" style="background:linear-gradient(135deg,#2a3c6a,#b8383a 55%,#e8e8e8)"></div><div class="label">Arbitration and ADR</div></div>
<div class="tile abs" style="left:601px;top:1458px"><div class="photo" role="img" aria-label="Balance scale and gavel on white" style="background:linear-gradient(135deg,#f4f4f4,#b8b8b8 60%,#7a4a2a)"></div><div class="label">Commercial and Corporate</div></div>
<div class="tile abs" style="left:852px;top:1458px"><div class="photo" role="img" aria-label="Hand holding prison bars" style="background:linear-gradient(90deg,#2a2a2a,#8a8a8a 50%,#3a3a3a)"></div><div class="label">Media Law</div></div>

<div class="btn abs" style="left:455px;top:1722px;width:290px;height:49px;font-size:20px">View All Practices</div>

<div class="malta-photo abs" role="img" aria-label="Team of smiling advocates in business attire"></div>
<h2 class="malta-title abs">About Malta</h2>
<div class="malta-text abs">
  <p>Lorem ipsum dolor sit amet, consectetur adipisicing elit, sed do eiusmod tempor incididunt ut labore et dolore magna aliqua. Ut enim ad minim veniam, quis nostrud exercitation ullamco laboris nisi ut aliquip ex ea commodo consequat. Duis aute irure dolor in reprehenderit in voluptate velit esse cillum dolore eu fugiat nulla pariatur.</p>
  <p>Excepteur sint occaecat cupidatat non proident, sunt in culpa qui officia deserunt mollit anim id est laborum. Sed ut perspiciatis unde omnis iste natus error sit voluptatem accusantium doloremque laudantium, totam rem aperiam, eaque ipsa quae ab illo inventore</p>
</div>
<div class="btn abs" style="left:505px;top:2252px;width:148px;height:35px;font-size:13px">Our Values</div>

<div class="testi-band abs"></div>
<div class="signin-band abs"></div>
<h2 class="section-title abs" style="top:2404px;width:806px;font-size:35px"><span>What Others Say</span></h2>
<span class="qmark abs" style="left:95px;top:2492px">&ldquo;</span>
<p class="quote abs">Lorem ipsum dolor sit amet, consectetur adipisicing elit, sed do eiusmod tempor incididunt ut labore et dolore magna aliqua. Ut enim ad minim veniam, quis nostrud exercitation ullamco laboris nisi ut aliquip ex ea commodo consequat. Duis aute irure dolor in reprehenderit in voluptate velit esse cillum dolore eu</p>
<span class="qmark abs" style="left:575px;top:2573px">&rdquo;</span>
<div class="avatar abs" role="img" aria-label="Client portrait"></div>
<div class="stars abs">★★★★★</div>
<div class="person abs">DANIEL MERCER<small>22 years</small></div>

<h2 class="section-title abs" style="left:734px;top:2420px;width:400px;font-size:30px"><span style="padding:0 14px">Sign In</span></h2>
<div class="field-label abs" style="top:2496px">E-MAIL</div>
<div class="field abs" style="top:2520px"></div>
<div class="field-label abs" style="top:2598px">PASSWORD</div>
<div class="forgot abs">Forgot password</div>
<div class="field abs" style="top:2621px"></div>
<svg class="abs" style="left:1070px;top:2632px" width="18" height="14" viewBox="0 0 18 14"><ellipse cx="9" cy="7" rx="8" ry="5" fill="none" stroke="#aaa" stroke-width="1.5"/><circle cx="9" cy="7" r="2.5" fill="#aaa"/></svg>
<div class="btn abs" style="left:852px;top:2701px;width:168px;height:43px;font-size:16px">Log In</div>
<div class="abs" style="left:734px;width:400px;top:2753px;text-align:center;font-size:9px;font-style:italic;color:var(--muted)">I don't have an account</div>

<footer>
  <div class="footer-dark abs"></div>
  <div class="footer-panel abs"></div>
  <svg class="abs" style="left:498px;top:2849px" width="603" height="335" viewBox="0 0 603 335"><polygon points="168,0 603,0 603,335 382,335" fill="#f7941d"/></svg>
  <h3 class="footer-title abs">Main Link</h3>
  <div class="footer-links">
    <a style="left:99px;top:2972px">Home</a><a style="left:262px;top:2972px">FAQs</a>
    <a style="left:99px;top:2996px">About us</a><a style="left:262px;top:2996px">Our Firm</a>
    <a style="left:99px;top:3021px">Practice Areas</a><a style="left:262px;top:3021px">Our Values</a>
    <a style="left:99px;top:3045px">About Malta</a><a style="left:262px;top:3045px">Latest news</a>
    <a style="left:99px;top:3071px">Contact</a><a style="left:262px;top:3071px">Office</a>
  </div>
  <svg class="abs" style="left:555px;top:2912px" width="96" height="24" viewBox="0 0 96 24" fill="none" stroke="#f7941d" stroke-width="1.5"><circle cx="12" cy="12" r="10"/><circle cx="47" cy="12" r="10"/><circle cx="82" cy="12" r="10"/></svg>
  <div class="footer-brand abs">Dalmer &amp; Vossen</div>
  <div class="address abs">12/4, Harbour Lane, Valletta<br>88, Olive Grove Street, Birkirkara</div>
  <div class="mail-link abs">✉ info@dvadvocates.example</div>

  <div class="phone abs" style="top:2918px"><svg width="22" height="22" viewBox="0 0 22 22"><rect x="1" y="1" width="20" height="20" fill="none" stroke="#fff" stroke-width="1.5"/><path d="M7 5l3 3-2 2a9 9 0 0 0 4 4l2-2 3 3-2 2C9 17 5 13 5 7z" fill="#fff"/></svg>(356) 2000 0145 (Birkirkara)</div>
  <div class="phone abs" style="top:2976px"><svg width="22" height="22" viewBox="0 0 22 22"><rect x="1" y="1" width="20" height="20" fill="none" stroke="#fff" stroke-width="1.5"/><path d="M7 5l3 3-2 2a9 9 0 0 0 4 4l2-2 3 3-2 2C9 17 5 13 5 7z" fill="#fff"/></svg>(356) 2000 0278 (Valletta)</div>
  <div class="phone abs" style="top:3031px"><svg width="24" height="22" viewBox="0 0 24 22" fill="#fff"><rect x="6" y="1" width="12" height="6"/><rect x="1" y="7" width="22" height="10" rx="2"/><rect x="6" y="13" width="12" height="8" fill="#f7941d" stroke="#fff" stroke-width="1.5"/></svg>(356) 2000 0390</div>
  <div class="phone abs" style="top:3088px;left:886px;font-family:'Lato',sans-serif;font-size:13px;font-weight:700"><svg width="22" height="16" viewBox="0 0 22 16"><rect x="1" y="1" width="20" height="14" fill="none" stroke="#fff" stroke-width="1.5"/><path d="M1 1l10 8 10-8" fill="none" stroke="#fff" stroke-width="1.5"/></svg>info@dvadvocates.example</div>

  <div class="bottom-bar abs">
    <div class="abs" style="left:99px;top:11px"><a>Home</a><a>Latest news</a><a>About</a><a>Site Map</a><a>Advocates</a><a>Terms and Privacy</a></div>
    <div class="abs" style="left:810px;top:11px;width:291px;text-align:right">Copyright 2016 Northgate Studio &nbsp;|&nbsp; All Rights Reserved</div>
  </div>
</footer>

</body>
</html>
```